Ecommerce site for Bramwell Dovey Company

This is an ecommerce store design and will be based on the xcart ecommerce platform, attached is a design specification and all images to use in the design, you may use any other images you see fit.
This is a new Company so has no logo, if possible please create a logo but if not just use a text based logo in the design this maybe replaced later if required.
We only require a Home page design initially but will also need a category and product page design created, if you can do those also it would be an advantage.
IMPORTANT
We require all designs to be supplied as a full size JPG so we can see the design in detail as the pixel quarry previews are often too small.

```html
<!DOCTYPE html>
<html lang="en">
<head>
<meta charset="utf-8">
<title>Bramwell Dovey Company – Home</title>
<link rel="stylesheet" href="https://fonts.googleapis.com/css2?family=Roboto+Condensed:wght@700&display=swap">
<style>
:root{
  --maroon:#3f1d20;
  --maroon-dark:#2e1214;
  --ink:#333;
  --body-text:#555;
  --bar-top:#4a4a4a;
  --bar-bottom:#2b2b2b;
  --page-bg:#ececec;
  --panel:#ffffff;
  --line:#d6d6d6;
  --box-bg:#f1f1f1;
}
*{box-sizing:border-box;margin:0;padding:0}
html,body{width:1200px;height:900px;overflow:hidden}
body{background:linear-gradient(#f4f4f4,var(--page-bg));font-family:Arial,Helvetica,sans-serif;color:var(--ink);position:relative}
.abs{position:absolute}
.top-rule{left:0;top:0;width:1200px;height:3px;background:#3a3a3a}
.account-tab{left:780px;top:0;width:311px;height:35px;background:#3a3a3a;border-radius:0 0 6px 6px;color:#fff;font-size:13px;display:flex;align-items:center;padding-left:12px}
.account-tab b{margin-right:6px}
.account-tab span{padding:0 6px;border-left:1px dotted #999}
.account-tab span:first-of-type{border-left:none}
.brand{left:108px;top:30px;font-family:"Roboto Condensed",sans-serif;font-weight:700;font-size:34px;color:#3d2a2b;letter-spacing:.5px;display:flex;align-items:center;gap:10px}
.brand i{display:block;width:14px;height:14px;background:var(--maroon)}
.search{left:846px;top:50px;display:flex}
.search .field{width:181px;height:25px;border:1px solid #c8c8c8;border-right:none;border-radius:4px 0 0 4px;background:#fff;font-size:12px;color:#888;padding:5px 9px}
.search .btn{width:64px;height:25px;background:var(--maroon);color:#fff;font-size:11px;font-weight:bold;border-radius:0 4px 4px 0;display:flex;align-items:center;justify-content:center}
.nav{left:108px;top:91px;width:983px;height:34px;background:linear-gradient(var(--bar-top),var(--bar-bottom));border-radius:4px;display:flex;align-items:center}
.nav a{color:#fff;font-size:13px;font-weight:bold;text-decoration:none;padding:0 16px;border-left:1px dotted #888;line-height:18px}
.nav a.current{background:#000;border:none;line-height:34px;padding:0 23px;border-radius:4px 0 0 4px}
.nav a.current + a{border-left:none}
.cart-area{left:822px;top:91px;width:269px;height:34px;background:linear-gradient(#8a8a8a,#5d5d5d);border-radius:17px 4px 4px 17px;display:flex;align-items:center;color:#fff;font-size:12px;font-weight:bold;padding-left:36px}
.cart-area svg{margin-right:4px}
.checkout{position:absolute;left:159px;top:6px;width:91px;height:22px;background:var(--maroon);border:1px solid #6b3a3d;border-radius:5px;font-size:11px;display:flex;align-items:center;justify-content:center;gap:5px}
.panel{left:108px;top:140px;width:983px;height:780px;background:var(--panel);border-radius:8px;box-shadow:0 0 6px rgba(0,0,0,.2)}
.box{left:117px;width:167px;border:1px solid #cfcfcf;border-radius:5px;background:linear-gradient(#fff,#e6e6e6);overflow:hidden}
.box h3{height:31px;background:var(--maroon);color:#fff;font-size:12.5px;font-weight:bold;padding:8px 13px;display:flex;align-items:center;gap:6px}
.box p{font-size:12px;color:#555;line-height:19px;padding:8px 15px}
.categories{top:151px;height:311px;background:#f3f3f3}
.categories li{list-style:none;height:25px;border-bottom:1px dashed #c2c2c2;font-size:12.5px;color:#444;padding:5px 15px;background:linear-gradient(#fafafa,#ededed)}
.categories .view-all{height:29px;background:#dedede;text-align:right;padding:7px 14px;font-size:12.5px;font-weight:bold;color:var(--maroon-dark);text-decoration:underline}
.select{margin:9px 11px;width:144px;height:17px;border:1px solid #999;font-size:12px;color:#555;padding:1px 4px;position:relative;background:#fff}
.select i{position:absolute;right:0;top:0;width:15px;height:15px;background:#ddd;border-left:1px solid #999}
.email{margin:9px 9px 7px;width:147px;height:24px;border:1px solid #c8c8c8;border-radius:8px;background:#fff;font-size:12px;color:#888;padding:4px 8px}
.submit{margin:0 10px 0 auto;width:54px;height:22px;background:var(--maroon);color:#fff;font-size:11px;font-weight:bold;border-radius:5px;display:flex;align-items:center;justify-content:center}
.hero{left:296px;top:151px;width:785px;height:214px;border-radius:4px;overflow:hidden;background:linear-gradient(180deg,#c9d1dc 0%,#aeb7c4 55%,#8d8a8f 100%);box-shadow:0 3px 5px rgba(0,0,0,.3)}
.hero-shade{position:absolute;left:0;top:0}
.hero ul{position:absolute;left:18px;top:119px;list-style:none;font-family:"Roboto Condensed",sans-serif;font-weight:700;font-size:16px;line-height:22px;color:#fff;text-transform:uppercase}
.hero li::before{content:"\2714";margin-right:5px}
.dots{left:1005px;top:383px;display:flex;gap:5px}
.dots i{width:9px;height:9px;background:#777}
.dots i:first-child{background:var(--maroon)}
.about-photo{left:312px;top:408px;width:200px;height:183px;background:linear-gradient(135deg,#d9d4cc,#f2efe9 55%,#c8d3a8)}
.about h2{position:absolute;left:539px;top:404px;font-size:18px;color:var(--maroon)}
.about .lead,.about .text{position:absolute;font-size:12.4px;line-height:21px;color:var(--body-text)}
.about .lead{left:539px;top:429px;width:510px}
.about .lead b{color:#333}
.about .text{left:312px;top:605px;width:760px}
.crumb{right:120px;top:733px;font-size:12.5px;color:#555}
.toolbar{left:296px;top:755px;width:785px;height:45px;background:var(--maroon);border-radius:3px;color:#fff;font-size:12.5px;display:flex;align-items:center}
.toolbar .seg{padding:0 8px 0 13px;border-right:1px solid #6c3a3e;height:45px;display:flex;align-items:center;gap:6px}
.toolbar .seg:last-child{border:none}
.drop{height:19px;background:#fff;color:#555;font-size:12px;padding:2px 6px;position:relative;border:1px solid #999}
.drop i{position:absolute;right:0;top:0;width:16px;height:17px;border-left:1px solid #999;background:#eee}
.grid-zone{left:296px;top:800px;width:785px;height:120px;background:#f1f1f1}
.card{top:818px;width:180px;height:100px;border:1px solid #d0d0d0;border-radius:5px;background:#fff}
.card div{margin:13px 14px;height:90px}
</style>
</head>
<body>
<div class="abs top-rule"></div>
<div class="abs account-tab"><b>Welcome!</b><span>Login</span><span>Create an account</span><span>Wish List</span></div>
<div class="abs brand"><i></i>BRAMWELL DOVEY</div>
<div class="abs search"><div class="field">Type text here</div><div class="btn">SEARCH</div></div>

<nav class="abs nav">
  <a class="current" href="#">HOME</a><a href="#">SEARCH</a><a href="#">CUSTOMER SERVICE</a><a href="#">ABOUT US</a><a href="#">FAQ</a><a href="#">CONTACT US</a>
</nav>
<div class="abs cart-area">
  <svg width="20" height="16" viewBox="0 0 20 16"><path d="M1 2h3l2 8h10l2-6H5" fill="none" stroke="#fff" stroke-width="1.8"/><circle cx="8" cy="13.5" r="1.6" fill="#fff"/><circle cx="15" cy="13.5" r="1.6" fill="#fff"/></svg>
  View cart (0)
  <div class="checkout">CHECK OUT <svg width="6" height="9"><path d="M0 0l6 4.5L0 9z" fill="#fff"/></svg></div>
</div>

<div class="abs panel"></div>

<aside>
  <div class="abs box categories">
    <h3>CATEGORIES ›</h3>
    <ul>
      <li>Option 1</li><li>Option 2</li><li>Option 3</li><li>Option 4</li><li>Option 5</li><li>Option 6</li><li>Option 7</li><li>Option 8</li><li>Option 9</li><li>Option 10</li>
    </ul>
    <div class="view-all">View All</div>
  </div>
  <div class="abs box" style="top:473px;height:74px"><h3>SELECT CURRENCY ›</h3><div class="select">US Dollar - USD<i></i></div></div>
  <div class="abs box" style="top:557px;height:111px"><h3>NEWSLETTER ›</h3><div class="email">Type email id here</div><div class="submit">SUBMIT</div></div>
  <div class="abs box" style="top:679px;height:87px"><h3>MY CART ›</h3><p>You have no items in your shopping cart.</p></div>
  <div class="abs box" style="top:776px;height:86px"><h3>COMPARE PRODUCTS ›</h3><p>You have no items to compare.</p></div>
  <div class="abs box" style="top:872px;height:60px"><h3>RECENTLY VIEWED ›</h3></div>
</aside>

<section class="abs hero" role="img" aria-label="Bright living room with a white sofa and tall windows">
  <svg class="hero-shade" width="785" height="214"><polygon points="0,107 410,107 530,214 0,214" fill="rgba(40,35,38,.78)"/></svg>
  <ul>
    <li>Free UK delivery on orders over £100</li>
    <li>Over 20 years experience measuring / making / fitting</li>
    <li>5 years guarantee on all Quietrail products</li>
    <li>Friendly family run business</li>
  </ul>
</section>
<div class="abs dots"><i></i><i></i><i></i><i></i><i></i></div>

<section class="about">
  <div class="abs about-photo" role="img" aria-label="Curtain poles in chrome, black and brass with glass finials beside flowers"></div>
  <h2>About Us</h2>
  <p class="lead"><b>Lorem ipsum dolor sit amet, consectetur adipiscing elit. Quisque eu eros nulla.</b><br>Pellentesque at massa nunc, non varius dui. Mauris vitae tellus in eros faucibus rutrum nec vestibulum ligula. Suspendisse potenti. Nulla facilisi. Suspendisse potenti. Suspendisse in ligula sem. Mauris iaculis, elit ac pharetra fringilla, metus lorem vestibulum elit, ut eleifend quam turpis id libero. Aenean sed vestibulum dui. Maecenas nulla nunc, semper sit amet consectetur vitae, lacinia vel libero. Nullam semper diam a nulla vestibulum fermentum. Pellentesque ullamcorper sapien et arcu elementum ac cursus arcu auctor. Mauris iaculis, elit ac pharetra fringilla, metus lorem vestibulum.</p>
  <p class="text">Lorem ipsum dolor sit amet, consectetur adipiscing elit. Quisque eu eros nulla. Pellentesque at massa nunc, non varius dui. Mauris vitae tellus in eros faucibus rutrum nec vestibulum ligula. Suspendisse potenti. Nulla facilisi. Suspendisse potenti. Suspendisse in ligula sem. Mauris iaculis, elit ac pharetra fringilla, metus lorem vestibulum elit, ut eleifend quam turpis id libero. Aenean sed vestibulum dui. Maecenas nulla nunc, semper sit amet consectetur vitae, lacinia vel libero. Nullam semper diam a nulla vestibulum fermentum. Pellentesque ullamcorper sapien et arcu elementum ac cursus arcu auctor.</p>
</section>

<div class="abs crumb">Home &gt; Gifts</div>

<div class="abs toolbar">
  <div class="seg">Items 1 to 25 of 127 total</div>
  <div class="seg">Sory by: <div class="drop" style="width:138px">Name<i></i></div></div>
  <div class="seg">Results per page: <div class="drop" style="width:45px">6<i></i></div></div>
  <div class="seg">View type:
    <svg width="16" height="10"><g fill="#fff"><rect width="4" height="4"/><rect x="6" width="4" height="4"/><rect x="12" width="4" height="4"/><rect y="6" width="4" height="4"/><rect x="6" y="6" width="4" height="4"/><rect x="12" y="6" width="4" height="4"/></g></svg> Grid
    <svg width="16" height="10" style="margin-left:8px"><g fill="#8a5a5e"><rect width="4" height="2"/><rect x="6" width="10" height="2"/><rect y="4" width="4" height="2"/><rect x="6" y="4" width="10" height="2"/><rect y="8" width="4" height="2"/><rect x="6" y="8" width="10" height="2"/></g></svg><span style="color:#8a5a5e">List</span> | <u>View All</u>
  </div>
</div>

<div class="abs grid-zone"></div>
<div class="abs card" style="left:310px"><div role="img" aria-label="Curtain track installed under a ceiling" style="background:linear-gradient(#8e8f93,#c7c4bf)"></div></div>
<div class="abs card" style="left:502px"><div role="img" aria-label="Sheer curtains on a window" style="background:linear-gradient(90deg,#b9b08a,#e6e1c9,#a89f7c)"></div></div>
<div class="abs card" style="left:693px"><div role="img" aria-label="White pleated curtain" style="background:linear-gradient(90deg,#2f3336,#e8e8e8 30%,#cfcfcf)"></div></div>
<div class="abs card" style="left:885px"><div role="img" aria-label="Bay window with curtains" style="background:linear-gradient(90deg,#b9a48f,#e8e2da,#b29c86)"></div></div>
</body>
</html>
```